Varnell Consulting needs a business card design

Varnell Consulting is a small business that consults and trains Australia wide in Workplace Health and Safety, Environment and Quality Management Systems.

Clients are typically smaller businesses with 50 to 200 employees but there are some large clients.

Communication is often by email, although mobile is used as well.

Varnell Consulting
47 Tessock Downs Road
Brayfield, QLD 4371
0438 291 604

```html
<!DOCTYPE html>
<html lang="en">
<head>
<meta charset="utf-8">
<title>Varnell Consulting — Business Card</title>
<link rel="stylesheet" href="https://fonts.googleapis.com/css2?family=Raleway:wght@300;500;600&family=Crimson+Text&display=swap">
<style>
  :root {
    --bg: #ebe9e6;
    --card-dark: #1c1c1e;
    --card-dark-mid: #2a2a2c;
    --accent: #2fb9ea;
    --white: #ffffff;
    --muted: #a9a9ab;
  }
  * { box-sizing: border-box; margin: 0; padding: 0; }
  html, body {
    width: 1200px; height: 1000px; overflow: hidden;
    background: var(--bg);
  }
  .canvas { position: relative; width: 1200px; height: 1000px; }

  .card {
    position: absolute;
    width: 560px; height: 320px;
    background: var(--card-dark);
    overflow: hidden;
    box-shadow: 0 6px 18px rgba(0,0,0,0.18);
  }
  .card--back  { left: 80px;  top: 140px; }
  .card--front { left: 560px; top: 540px; }

  .card__texture {
    position: absolute; top: 0; bottom: 0;
    background: radial-gradient(ellipse at 55% 40%, var(--card-dark-mid) 0%, var(--card-dark) 75%);
  }
  .card--back  .card__texture { left: 0; width: 508px; }
  .card--front .card__texture { left: 52px; right: 0; }

  .stripe { position: absolute; top: 0; bottom: 0; }
  .stripe--accent { background: var(--accent); }
  .stripe--white  { background: var(--white); }
  .card--back  .stripe--accent { left: 508px; width: 16px; }
  .card--back  .stripe--white  { left: 524px; width: 36px; }
  .card--front .stripe--accent { left: 0; width: 38px; }
  .card--front .stripe--white  { left: 38px; width: 14px; }

  .brand { position: absolute; font-family: "Raleway", sans-serif; }
  .brand__name {
    font-weight: 500; font-size: 23px; letter-spacing: 0.5px;
    color: var(--white); text-transform: uppercase; white-space: nowrap;
  }
  .brand__person {
    margin-top: 4px;
    font-weight: 300; font-size: 17px; color: var(--muted);
    white-space: nowrap;
  }

  .card--back  .brand { left: 175px; top: 38px; }
  .card--front .brand { left: 175px; top: 130px; }

  .contact {
    position: absolute; left: 26px; bottom: 34px;
    font-family: "Crimson Text", serif; font-size: 13px;
    color: var(--muted); line-height: 1.35;
  }
  .contact__label { color: var(--accent); }
  .contact__phone {
    font-family: "Raleway", sans-serif; font-weight: 600;
    color: var(--white);
  }
</style>
</head>
<body>
<main class="canvas">

  <section class="card card--back" aria-label="Business card, contact side">
    <div class="card__texture" role="img" aria-label="Dark charcoal background with a subtle square grid pattern"></div>
    <div class="stripe stripe--accent"></div>
    <div class="stripe stripe--white"></div>

    <div class="brand">
      <p class="brand__name">Varnell Consulting</p>
      <p class="brand__person">Owen Varnell</p>
    </div>

    <div class="contact">
      <p><span class="contact__label">e:</span>ovarnell@tessmail.net.au</p>
      <p class="contact__phone"><span class="contact__label">t:</span> 0438 291 604</p>
      <p><span class="contact__label">a:</span>47 Tessock Downs Road Brayfield, QLD 4371</p>
    </div>
  </section>

  <section class="card card--front" aria-label="Business card, name side">
    <div class="stripe stripe--accent"></div>
    <div class="stripe stripe--white"></div>
    <div class="card__texture" role="img" aria-label="Dark charcoal background with a subtle square grid pattern"></div>

    <div class="brand">
      <p class="brand__name">Varnell Consulting</p>
      <p class="brand__person">Owen Varnell</p>
    </div>
  </section>

</main>
</body>
</html>
```